Zielgruppe
Zeitarbeit Personalvermittlung Arbeitsvermittlung Arbeitnehmerüberlassung
Zielgruppe:
Akademiker
Fachkräfte
Politiker
Ingenieur
wichtige Akteure der Gesellschaft
Kommunen
Vereinigungen
Aufgabenstellung
Wir benötigen schlichte und dezente, aber eindrucksvolle,exklusive Visitenkarten mit unserem Logo.
Aufbau:
Vorname, Name
Position
Telefon
Mobil
E-Mail
Fax
Unsere Website: http://www.velmaris-personal.de
Wir sind 2 Geschäftsführer also bitte für beide Namen
Dies benötigen wir als PSD, PDF, JPG, sodass wir selbst die Angaben nach Belieben eintragen können.

```html
<!DOCTYPE html>
<html lang="de">
<head>
<meta charset="utf-8">
<title>Velmaris – Visitenkarten</title>
<link href="https://fonts.googleapis.com/css2?family=Inter:ital,wght@0,300;0,400;0,500;1,300&display=swap" rel="stylesheet">
<style>
  :root {
    --orange: #ff5a00;
    --orange-light: #ff8a00;
    --ink: #2a2a2a;
    --text: #555;
    --frame: #333;
    --paper: #fff;
  }
  html, body { margin: 0; padding: 0; overflow: hidden; }
  body {
    width: 849px; height: 1200px; position: relative;
    background: var(--paper);
    font-family: "Inter", Arial, sans-serif;
  }
  .card {
    position: absolute; width: 222px; height: 343px;
    border: 1px solid var(--frame); box-sizing: border-box;
    background: var(--paper); overflow: hidden;
  }
  .card--front-a { left: 179px; top: 98px; }
  .card--back-a  { left: 442px; top: 98px; }
  .card--front-b { left: 179px; top: 706px; }
  .card--back-b  { left: 442px; top: 706px; }

  .line { position: absolute; left: 0; right: 0; text-align: center; white-space: nowrap; }

  .brand {
    top: 222px; font-size: 27px; font-weight: 300; color: var(--ink);
    letter-spacing: -0.5px;
  }
  .brand__dot {
    display: inline-block; width: 12px; height: 12px; border-radius: 50%;
    background: var(--orange); margin-right: 6px; vertical-align: 3px;
  }

  .name  { top: 70px; font-size: 16px; font-weight: 500; color: var(--orange); }
  .role  { top: 89px; font-size: 13px; font-weight: 300; font-style: italic; color: var(--text); }
  .contact { font-size: 7.5px; font-weight: 300; color: var(--text); }
  .contact .sep { color: var(--orange); margin: 0 2px; }
  .web { font-size: 10px; font-weight: 300; color: var(--orange); }

  .card--back-a .c1 { top: 166px; }
  .card--back-a .c2 { top: 178px; }
  .card--back-a .c3 { top: 198px; }
  .card--back-a .c4 { top: 218px; }
  .card--back-a .web { top: 303px; }

  .card--back-b .c1 { top: 143px; }
  .card--back-b .c2 { top: 155px; }
  .card--back-b .c3 { top: 175px; }
  .card--back-b .c4 { top: 195px; }
  .card--back-b .web { top: 234px; }

  .wave {
    position: absolute; left: 0; right: 0; bottom: 0; height: 58px;
    background: linear-gradient(90deg, var(--orange) 0%, var(--orange-light) 50%, var(--orange) 100%);
  }
</style>
</head>
<body>
  <section class="card card--front-a">
    <div class="line brand"><span class="brand__dot"></span>velmaris</div>
  </section>

  <section class="card card--back-a">
    <div class="line name">Lukas Marenko</div>
    <div class="line role">Geschäftsführung</div>
    <div class="line contact c1">Telefon<span class="sep">•</span>02356 – 48 71 20</div>
    <div class="line contact c2">Mobil<span class="sep">•</span>0171 5509874</div>
    <div class="line contact c3">E-Mail<span class="sep">•</span>marenko@velmaris-personal.de</div>
    <div class="line contact c4">Fax<span class="sep">•</span>02356 – 48 71 29</div>
    <div class="line web">www.velmaris-personal.de</div>
  </section>

  <section class="card card--front-b">
    <div class="line brand"><span class="brand__dot"></span>velmaris</div>
    <div class="wave" role="img" aria-label="Orangefarbene Wellen-Dekoration"></div>
  </section>

  <section class="card card--back-b">
    <div class="line name">Lukas Marenko</div>
    <div class="line role">Geschäftsführung</div>
    <div class="line contact c1">Telefon<span class="sep">•</span>02356 – 48 71 20</div>
    <div class="line contact c2">Mobil<span class="sep">•</span>0171 5509874</div>
    <div class="line contact c3">E-Mail<span class="sep">•</span>marenko@velmaris-personal.de</div>
    <div class="line contact c4">Fax<span class="sep">•</span>02356 – 48 71 29</div>
    <div class="line web">www.velmaris-personal.de</div>
    <div class="wave" role="img" aria-label="Orangefarbene Wellen-Dekoration"></div>
  </section>
</body>
</html>
```